Delvin & Associates - London New Letting and Property Management Company *

Delvin & Associates LTD is a new company based in London, and works with brand new residential property in the city centre.

We are aiming to have 1000 new properties a year.

We are looking for something modern and minimalistic :
Logo ,Monogram, Paper Head and Business Card.

Target Market(s)

Internation landlords

Industry/Entity Type

Real Estate

Logo Text

Delvin & Associates

Colors

Designer to choose colors to be used in the design.

Requirements
Nice to have
• A particular monogram with "DA"
Should not have
• Little House over the logo

```html
<!DOCTYPE html>
<html lang="en">
<head>
<meta charset="utf-8">
<title>Delvin &amp; Associates – Stationery</title>
<link href="https://fonts.googleapis.com/css2?family=Lato:wght@400;700&family=Montserrat:wght@400;500;600;700&display=swap" rel="stylesheet">
<style>
:root{
  --bg:#d9d9d9;
  --paper:#f2f2f2;
  --navy:#1c4e70;
  --sky:#27a6e0;
  --ink:#6b6b6b;
  --ink-dark:#555555;
}
*{margin:0;padding:0;box-sizing:border-box}
html,body{width:1200px;height:1062px;overflow:hidden;background:var(--bg)}
body{position:relative;font-family:'Montserrat',sans-serif;color:var(--ink)}
.sheet,.card{position:absolute;background:var(--paper);box-shadow:0 2px 6px rgba(0,0,0,.18)}
.letterhead{left:116px;top:94px;width:618px;height:875px}
.brand{position:absolute;display:flex;align-items:center;gap:6px;font-family:'Montserrat',sans-serif;font-weight:700;color:var(--navy);text-transform:uppercase;letter-spacing:.02em}
.brand .mark{background:var(--navy);flex:none}
.letterhead .brand{left:45px;top:44px;width:120px;flex-direction:column;align-items:flex-start;font-size:8px;gap:5px}
.letterhead .brand .mark{width:40px;height:40px}
.divider{position:absolute;width:2px;background:var(--navy)}
.letterhead .divider{left:280px;top:44px;height:75px}
.contact{position:absolute;font-size:11px;line-height:15px;color:var(--ink)}
.contact .addr{margin-bottom:6px}
.contact .row{display:flex;align-items:center;gap:5px}
.contact svg{width:7px;height:7px;flex:none}
.contact b{font-weight:600;color:var(--navy)}
.letterhead .contact{left:424px;top:42px}
.date{position:absolute;left:45px;top:195px;font-size:11px;font-weight:500;color:var(--ink-dark)}
.recipient{position:absolute;left:45px;top:222px;font-family:'Lato',sans-serif;color:var(--ink-dark)}
.recipient .name{font-size:14.5px;line-height:18px}
.recipient .role,.recipient .org{font-size:11px;line-height:16px}
.recipient .street{font-family:'Montserrat',sans-serif;font-size:9.5px;line-height:13px;margin-top:2px}
.body{position:absolute;left:45px;top:336px;width:530px;font-size:11.6px;line-height:16px;color:var(--ink)}
.body p{margin-bottom:20px}
.closing{position:absolute;left:45px;top:718px;font-family:'Lato',sans-serif;color:var(--ink-dark)}
.closing .regards{font-size:14.5px}
.signature{display:block;width:110px;height:18px;margin:10px 0 8px;background:linear-gradient(90deg,#8a8a8a33,#6b6b6b55,#8a8a8a22);border-radius:9px}
.closing .name{font-size:14px;line-height:17px}
.closing .role{font-size:11px;line-height:15px}
.closing .org{font-size:8px;font-weight:700;text-transform:uppercase;line-height:13px}
.brand-showcase{left:878px;top:152px;width:212px;flex-direction:column;gap:16px;font-size:17px;align-items:center}
.brand-showcase .mark{width:190px;height:190px}
.card-light{left:717px;top:476px;width:372px;height:211px}
.card-light .brand{left:38px;top:58px;width:92px;flex-direction:column;gap:8px;font-size:8px;text-align:center}
.card-light .brand .mark{width:62px;height:62px}
.card-light .divider{left:167px;top:58px;height:98px;width:1.5px}
.card-light .person{position:absolute;left:201px;top:54px}
.person .name{font-size:16px;font-weight:500;color:var(--navy);letter-spacing:.02em;line-height:20px}
.person .title{font-size:9px;line-height:13px;margin-bottom:5px}
.card-light .contact{position:static;font-size:9px;line-height:13px}
.card-light .contact .addr{margin-bottom:4px}
.card-dark{left:717px;top:727px;width:372px;height:211px;background:var(--navy)}
.card-dark .brand{left:136px;top:48px;width:100px;flex-direction:column;gap:10px;font-size:8.5px;color:#fff;text-align:center}
.card-dark .brand .mark{width:70px;height:70px;background:var(--sky)}
</style>
</head>
<body>

<section class="sheet letterhead">
  <div class="brand"><span class="mark"></span><span>Delvin &amp; Associates</span></div>
  <span class="divider"></span>
  <div class="contact">
    <div class="addr">12 Harlow Row<br>London EC2A 4BX</div>
    <div class="row"><svg viewBox="0 0 8 8"><path d="M1.5 0.5l1.5 0 0.5 2-1 .8a4 4 0 0 0 2.2 2.2l.8-1 2 .5 0 1.5C5 7 1 3 1.5.5z" fill="#1c4e70"/></svg>+44 20 7946 0321</div>
    <div class="row"><svg viewBox="0 0 8 8"><rect x=".5" y="1.5" width="7" height="5" fill="none" stroke="#1c4e70"/><path d="M.5 1.5l3.5 3 3.5-3" fill="none" stroke="#1c4e70"/></svg>info@delvinassociates.com</div>
    <div class="row"><svg viewBox="0 0 8 8"><circle cx="4" cy="4" r="3.5" fill="none" stroke="#1c4e70"/><path d="M.5 4h7M4 .5c-2 2-2 5 0 7M4 .5c2 2 2 5 0 7" fill="none" stroke="#1c4e70" stroke-width=".7"/></svg>www.<b>delvinassociates</b>.com</div>
  </div>

  <p class="date">8th November 2018</p>
  <div class="recipient">
    <p class="name">Oliver Grant</p>
    <p class="role">Founder</p>
    <p class="org">Grant Advisory Group</p>
    <p class="street">88 Wexford Lane, Bristol,<br>BS1 5QT</p>
  </div>

  <div class="body">
    <p>Lorem ipsum dolor sit amet, an vel recteque dissentiet, detracto albucius platonem ex vel, eros repudiandae cu. Atqui aliquando nec an, unum graece adolescens vel ad. Id odio scae has, iudico euismod atomorum ius ea, cum ea honestatis quaerendum theophrastus. Mea honestatis quaerendum theophrastus. Mea</p>
    <p>Lorem ipsum dolor sit amet, an vel recteque dissentiet, detracto albucius platonem ex vel, eros repudiandae cu. Atqui aliquando nec an, unum graece adolescens vel ad. Id odio scae has, iudico euismod atomorum ius ea, cum ea honestatis quaerendum theophrastus. Mea doming repudiandae ex, cu cum civibus assentior posidonium. Quo etiam pertinax ex, te eros repudiandae cu. Atqui aliquando nec an, unum graece adolescens vel ad. Id odio scae honestatis quaerendum theophrastus. Mea</p>
    <p>Lorem ipsum dolor sit amet, an vel recteque dissentiet, detracto albucius platonem ex vel, eros repudiandae cu. Atqui aliquando nec an, unum graece adolescens vel ad. Id odio scae has, iudico euismod atomorum ius ea, cum ea honestatis quaerendum theophrastus. Mea honestatis quaerendum theophrastus. Mea</p>
    <p>Lorem ipsum dolor sit amet, an vel recteque dissentiet, detracto albucius platonem ex vel, eros repudiandae cu. Atqui aliquando nec an, unum graece adolescens vel ad. Id odio scae has, iudico euismod atomorum ius ea, cum ea honestatis quaerendum theophrastus. Mea honestatis quaerendum theophrastus. Mea</p>
  </div>

  <div class="closing">
    <p class="regards">Kind Regards</p>
    <span class="signature" role="img" aria-label="Handwritten signature of Edward Collins"></span>
    <p class="name">Edward Collins</p>
    <p class="role">Chief Alchemist</p>
    <p class="org">Delvin &amp; Associates LTD</p>
  </div>
</section>

<div class="brand brand-showcase"><span class="mark"></span><span>Delvin &amp; Associates</span></div>

<section class="card card-light">
  <div class="brand"><span class="mark"></span><span>Delvin &amp; Associates</span></div>
  <span class="divider"></span>
  <div class="person">
    <p class="name">THOMAS REED</p>
    <p class="title">Director</p>
    <div class="contact">
      <div class="addr">12 Harlow Row<br>London EC2A 4BX</div>
      <div class="row"><svg viewBox="0 0 8 8"><path d="M1.5 0.5l1.5 0 0.5 2-1 .8a4 4 0 0 0 2.2 2.2l.8-1 2 .5 0 1.5C5 7 1 3 1.5.5z" fill="#1c4e70"/></svg>+44 20 7946 0321</div>
      <div class="row"><svg viewBox="0 0 8 8"><rect x=".5" y="1.5" width="7" height="5" fill="none" stroke="#1c4e70"/><path d="M.5 1.5l3.5 3 3.5-3" fill="none" stroke="#1c4e70"/></svg>info@delvinassociates.com</div>
      <div class="row"><svg viewBox="0 0 8 8"><circle cx="4" cy="4" r="3.5" fill="none" stroke="#1c4e70"/><path d="M.5 4h7M4 .5c-2 2-2 5 0 7M4 .5c2 2 2 5 0 7" fill="none" stroke="#1c4e70" stroke-width=".7"/></svg>www.<b>delvinassociates</b>.com</div>
    </div>
  </div>
</section>

<section class="card card-dark">
  <div class="brand"><span class="mark"></span><span>Delvin &amp; Associates</span></div>
</section>

</body>
</html>
```